stationary
envelopes, letterhead, biz card
I need single sided standard sized Business Card [3.5" x 2"]
doesnt matter whatever looks good
Professional
Marten Olufsson
President
4218 Wexhollow Ave Ste 202-517
marten@bexlin.com
www.bexlin.com

```html
<!DOCTYPE html>
<html lang="en">
<head>
<meta charset="utf-8">
<title>Bexlin – Business Cards</title>
<link rel="stylesheet" href="https://fonts.googleapis.com/css2?family=Montserrat:wght@400;500;700&display=swap">
<style>
  :root {
    --backdrop: #1c1c1e;
    --card-white: #f4f4f4;
    --card-white-edge: #d6d6d6;
    --card-dark: #232325;
    --card-dark-deep: #151517;
    --accent-blue: #1f9ad6;
    --ink-dark: #1d1d1f;
    --ink-light: #d8d8d8;
    --ink-muted: #a9a9a9;
  }
  * { box-sizing: border-box; margin: 0; padding: 0; }
  html, body {
    width: 1200px;
    height: 901px;
    overflow: hidden;
    background: var(--backdrop);
    font-family: "Montserrat", "Helvetica Neue", Arial, sans-serif;
  }
  .card {
    position: absolute;
    left: 290px;
    width: 620px;
    height: 354px;
    border-radius: 16px;
    overflow: hidden;
    box-shadow: 0 16px 40px rgba(0,0,0,0.55);
  }
  .brand {
    position: absolute;
    display: flex;
    align-items: center;
  }
  .brand-mark { background: var(--accent-blue); flex: none; }
  .brand-name {
    font-weight: 700;
    color: var(--ink-dark);
    line-height: 1;
    letter-spacing: 1px;
  }

  /* Back side: logo only */
  .card-back {
    top: 50px;
    background: linear-gradient(180deg, #ffffff 0%, var(--card-white) 65%, var(--card-white-edge) 100%);
  }
  .card-back .brand {
    left: 50%;
    top: 50%;
    transform: translate(-50%, -50%);
    gap: 22px;
  }
  .card-back .brand-mark { width: 54px; height: 54px; }
  .card-back .brand-name { font-size: 76px; }

  /* Front side */
  .card-front {
    top: 450px;
    background: var(--card-dark);
  }
  .card-top {
    position: absolute;
    inset: 0 0 auto 0;
    height: 162px;
    background: linear-gradient(180deg, #ffffff 0%, var(--card-white) 70%, var(--card-white-edge) 100%);
  }
  .card-front .brand { left: 60px; top: 52px; gap: 16px; }
  .card-front .brand-mark { width: 40px; height: 40px; }
  .card-front .brand-name { font-size: 57px; }
  .card-bottom {
    position: absolute;
    inset: 162px 0 0 0;
    background: linear-gradient(180deg, var(--card-dark) 0%, var(--card-dark-deep) 100%);
  }
  .texture-panel {
    position: absolute;
    right: 0;
    top: 170px;
    width: 240px;
    bottom: 0;
    background: radial-gradient(ellipse at 70% 40%, rgba(255,255,255,0.07) 0%, rgba(255,255,255,0.02) 55%, rgba(255,255,255,0) 80%);
  }
  .accent-rule {
    position: absolute;
    left: 0;
    right: 0;
    top: 162px;
    height: 8px;
    background: var(--accent-blue);
  }
  .name-band {
    position: absolute;
    left: 0;
    top: 153px;
    width: 453px;
    height: 41px;
    background: var(--accent-blue);
    display: flex;
    align-items: center;
    padding-left: 60px;
    color: #ffffff;
    font-size: 18px;
  }
  .holder-name { font-weight: 500; letter-spacing: 0.3px; }
  .holder-title {
    font-weight: 400;
    margin-left: 14px;
    padding-left: 14px;
    border-left: 1.5px solid rgba(255,255,255,0.85);
    line-height: 1.1;
  }
  .address {
    position: absolute;
    left: 60px;
    top: 228px;
    font-size: 15px;
    font-style: normal;
    line-height: 1.45;
    color: var(--ink-light);
  }
  .contact-list {
    position: absolute;
    left: 347px;
    top: 214px;
    list-style: none;
    font-size: 14px;
    line-height: 1.5;
    color: var(--ink-light);
  }
  .contact-list .label { color: var(--ink-muted); }
  .website {
    position: absolute;
    left: 385px;
    top: 298px;
    font-size: 15px;
    color: var(--ink-light);
  }
  .website strong { font-weight: 700; color: #ffffff; }
</style>
</head>
<body>
  <section class="card card-back" aria-label="Bexlin business card, back">
    <div class="brand">
      <span class="brand-mark" aria-hidden="true"></span>
      <span class="brand-name">BEXLIN</span>
    </div>
  </section>

  <main class="card card-front" aria-label="Bexlin business card, front">
    <section class="card-top">
      <div class="brand">
        <span class="brand-mark" aria-hidden="true"></span>
        <span class="brand-name">BEXLIN</span>
      </div>
    </section>
    <section class="card-bottom"></section>
    <div class="texture-panel" role="img" aria-label="Faint tonal decorative texture on the dark panel"></div>
    <div class="accent-rule" aria-hidden="true"></div>
    <div class="name-band">
      <span class="holder-name">Marten Olufsson</span>
      <span class="holder-title">President</span>
    </div>
    <address class="address">
      4218 Wexhollow Ave<br>Ste 202-517
    </address>
    <ul class="contact-list">
      <li><span class="label">P:</span> 555.214.0386</li>
      <li><span class="label">F:</span> 555.730.6419</li>
      <li><span class="label">E:</span> marten@bexlin.com</li>
    </ul>
    <p class="website">www.<strong>bexlin</strong>.com</p>
  </main>
</body>
</html>
```